Quillo Business Card Design

Looking for elegant and super stylish business cards. Enclosed is the card design we are using now. We need something more contemporary.

Target Market(s)

We are a catering company focusing on weddings and corporate events.

Industry/Entity Type

Caterer

Contact Information for Business Card

Please use similar font to our current cards

Colors
0592cd

Requirements
Must have
• Color and be very unique. Also, please use logo (with or without the castle.)

```html
<!DOCTYPE html>
<html lang="en">
<head>
<meta charset="utf-8">
<title>Quillo Catering – Business Card</title>
<link rel="stylesheet" href="https://fonts.googleapis.com/css2?family=Caveat+Brush&family=Open+Sans:wght@400&display=swap">
<style>
  :root {
    --backdrop: #e4e5e7;
    --card-dark: #21222a;
    --card-light: #ffffff;
    --gold: #fbb123;
    --gold-soft: rgba(251, 177, 35, 0.55);
    --ink-light: #ffffff;
    --ink-dark: #111111;
  }
  * { box-sizing: border-box; margin: 0; padding: 0; }
  html, body {
    width: 1200px; height: 1200px; overflow: hidden;
    background: var(--backdrop);
  }
  .canvas { position: relative; width: 1200px; height: 1200px; }

  .card {
    position: absolute; top: 251px;
    width: 417px; height: 717px;
    background: var(--card-dark);
    overflow: hidden;
  }
  .card--front { left: 124px; }
  .card--back { left: 658px; }

  .card__header {
    position: absolute; left: 0; top: 0;
    width: 100%; height: 303px;
    background: var(--card-light);
  }

  .rule { position: absolute; background: var(--gold); }
  .rule--h { height: 4px; }
  .rule--v { width: 4px; }

  .ornament {
    position: absolute; width: 88px; height: 94px;
    background: radial-gradient(circle at center, var(--gold-soft) 0%, rgba(251,177,35,0.25) 45%, rgba(251,177,35,0) 72%);
  }

  /* Front brand name */
  .brand-name {
    position: absolute; left: 0; top: 326px; width: 100%;
    font-family: "Open Sans", sans-serif; font-weight: 400;
    font-size: 52px; line-height: 64px; letter-spacing: 4px;
    color: var(--ink-light); text-align: center; white-space: nowrap;
  }

  /* Back identity */
  .person__name {
    position: absolute; left: 71px; top: 186px; width: 273px;
    font-family: "Caveat Brush", cursive; font-size: 36px; line-height: 1;
    letter-spacing: 4px; color: var(--ink-dark); text-align: center;
    white-space: nowrap;
  }
  .person__rule {
    position: absolute; left: 91px; top: 242px;
    width: 233px; height: 3px; background: var(--ink-dark);
  }
  .person__title {
    position: absolute; left: 91px; top: 253px; width: 233px;
    font-family: "Open Sans", sans-serif; font-size: 13px;
    letter-spacing: 2.4px; color: var(--ink-dark);
    text-align: center; text-transform: uppercase; white-space: nowrap;
  }

  .contact {
    position: absolute;
    font-family: "Open Sans", sans-serif; font-size: 15px; line-height: 19px;
    letter-spacing: 1.1px; color: var(--ink-light); white-space: nowrap;
  }
  .contact__icon { position: absolute; fill: var(--ink-light); }
</style>
</head>
<body>
<main class="canvas">

  <section class="card card--front" aria-label="Card front">
    <div class="ornament" style="left:16px;top:46px" role="img" aria-label="Gold corner flourish"></div>
    <div class="ornament" style="left:314px;top:46px" role="img" aria-label="Gold corner flourish"></div>
    <div class="ornament" style="left:16px;top:590px" role="img" aria-label="Gold corner flourish"></div>
    <div class="ornament" style="left:314px;top:590px" role="img" aria-label="Gold corner flourish"></div>
    <span class="rule rule--h" style="left:112px;top:52px;width:192px"></span>
    <span class="rule rule--h" style="left:112px;top:675px;width:192px"></span>
    <span class="rule rule--v" style="left:18px;top:150px;height:431px"></span>
    <span class="rule rule--v" style="left:394px;top:150px;height:431px"></span>

    <h1 class="brand-name">Quillo</h1>
  </section>

  <section class="card card--back" aria-label="Card back">
    <div class="card__header"></div>
    <div class="ornament" style="left:18px;top:27px" role="img" aria-label="Gold corner flourish"></div>
    <div class="ornament" style="left:310px;top:27px" role="img" aria-label="Gold corner flourish"></div>
    <div class="ornament" style="left:18px;top:593px" role="img" aria-label="Gold corner flourish"></div>
    <div class="ornament" style="left:310px;top:593px" role="img" aria-label="Gold corner flourish"></div>
    <span class="rule rule--h" style="left:115px;top:30px;width:187px"></span>
    <span class="rule rule--h" style="left:115px;top:680px;width:187px"></span>
    <span class="rule rule--v" style="left:23px;top:132px;height:449px"></span>
    <span class="rule rule--v" style="left:389px;top:132px;height:449px"></span>

    <h2 class="person__name">Marlo Venteri</h2>
    <span class="person__rule"></span>
    <p class="person__title">Chief Executive Officer</p>

    <svg class="contact__icon" style="left:112px;top:359px" width="14" height="14" viewBox="0 0 24 24" aria-hidden="true"><path d="M6.6 10.8a15.1 15.1 0 0 0 6.6 6.6l2.2-2.2a1 1 0 0 1 1-.25 11.4 11.4 0 0 0 3.6.57 1 1 0 0 1 1 1V20a1 1 0 0 1-1 1A17 17 0 0 1 3 4a1 1 0 0 1 1-1h3.5a1 1 0 0 1 1 1c0 1.25.2 2.45.57 3.57a1 1 0 0 1-.25 1z"/></svg>
    <p class="contact" style="left:130px;top:357px">555 014 2087 ext. 312<br>555 017 4431</p>

    <svg class="contact__icon" style="left:99px;top:425px" width="15" height="11" viewBox="0 0 24 18" aria-hidden="true"><path d="M0 0h24v18H0z M2 2v1l10 7 10-7V2z" fill-rule="evenodd"/></svg>
    <p class="contact" style="left:118px;top:421px">m@thequillocatering.com</p>

    <svg class="contact__icon" style="left:88px;top:466px" width="12" height="16" viewBox="0 0 24 32" aria-hidden="true"><path d="M12 0a12 12 0 0 0-12 12c0 9 12 20 12 20s12-11 12-20A12 12 0 0 0 12 0zm0 17a5 5 0 1 1 0-10 5 5 0 0 1 0 10z"/></svg>
    <p class="contact" style="left:109px;top:464px">4120 Larkspur Lane<br>Port Halden California 90412</p>

    <svg class="contact__icon" style="left:88px;top:520px" width="13" height="13" viewBox="0 0 24 24" aria-hidden="true"><path d="M24 0 0 10l10 4 4 10z"/></svg>
    <p class="contact" style="left:106px;top:517px">www.thequillocatering.com</p>
  </section>

</main>
</body>
</html>
```